Gentleman's grooming products require a business card

I need a business card that incorporates the logo [ or parts of ] that we had Pixel Hive design for us as uploaded.

We sell online, mens grooming products including moustache waxes, beard oils and shaving accessories.
We want a card that is classy, professional and a card that shouts mens products.

Target Market(s)

Young professional male market

Industry/Entity Type

Business

Contact Information for Business Card

Ross and Edith Carwell
Lather and Lore
Purveyors of gentleman's stiffeners and grooming requisites
M :0418529647
E : ross@latherandlore.com.au
E : edith@latherandlore.com.au
E : sales@theblokesbalmery.com.au

W : www.latherandlore.com.au

Requirements
Must have
• Class
Nice to have
• Professionalism

```html
<!DOCTYPE html>
<html lang="en">
<head>
<meta charset="utf-8">
<title>Lather and Lore — Business Card</title>
<link href="https://fonts.googleapis.com/css2?family=Open+Sans:wght@400;600&family=Cormorant+Garamond:wght@500&display=swap" rel="stylesheet">
<style>
  :root{
    --backdrop:#2a2a2c;
    --card:#1b1b1d;
    --ink:#ffffff;
    --gold:#e3b71d;
    --muted:#d9d9d9;
  }
  *{box-sizing:border-box;margin:0;padding:0}
  html,body{width:1200px;height:1189px;overflow:hidden}
  body{
    background:var(--backdrop);
    font-family:"Open Sans",Arial,sans-serif;
    color:var(--ink);
    position:relative;
  }
  .card{
    position:absolute;left:170px;width:860px;height:480px;
    background:var(--card);border-radius:34px;
    box-shadow:0 14px 40px rgba(0,0,0,.55);
    overflow:hidden;
  }
  .card--front{top:80px}
  .card--back{top:630px}

  .brand{display:flex;flex-direction:column;align-items:center}
  .brand__row{display:flex;align-items:center;gap:18px}
  .brand__square{width:40px;height:40px;border:2px solid var(--ink)}
  .brand__name{font-size:54px;font-weight:400;letter-spacing:1px;color:var(--ink);white-space:nowrap}
  .brand__tagline{
    margin-top:14px;font-family:"Cormorant Garamond",Georgia,serif;font-weight:500;
    font-size:14px;letter-spacing:3px;text-transform:uppercase;color:var(--muted);
    white-space:nowrap;
  }

  .card--front .brand{position:absolute;left:0;right:0;top:150px}
  .website{
    position:absolute;left:0;right:0;top:330px;text-align:center;
    font-size:22px;font-weight:600;color:var(--gold);letter-spacing:.3px;
  }

  .card--back .brand{position:absolute;left:0;right:0;top:60px}
  .names{
    position:absolute;left:0;right:0;top:232px;display:flex;align-items:center;
  }
  .names__rule{flex:1;height:2px;background:var(--gold)}
  .names__text{padding:0 18px;font-size:28px;font-weight:400;letter-spacing:1px;text-transform:uppercase;white-space:nowrap}
  .contacts{
    position:absolute;left:0;right:0;top:292px;
    display:flex;flex-direction:column;align-items:center;gap:6px;
    font-size:23px;
  }
  .contacts__label{color:var(--gold);margin-right:8px}
</style>
</head>
<body>
  <section class="card card--front">
    <div class="brand">
      <div class="brand__row">
        <span class="brand__square"></span>
        <span class="brand__name">Lather and Lore</span>
      </div>
      <p class="brand__tagline">Makers of fine beard balms, moustache waxes and shaving goods</p>
    </div>
    <p class="website">www.latherandlore.com.au</p>
  </section>

  <section class="card card--back">
    <div class="brand">
      <div class="brand__row">
        <span class="brand__square"></span>
        <span class="brand__name">Lather and Lore</span>
      </div>
      <p class="brand__tagline">Makers of fine beard balms, moustache waxes and shaving goods</p>
    </div>
    <div class="names">
      <span class="names__rule"></span>
      <span class="names__text">Ross and Edith Carwell</span>
      <span class="names__rule"></span>
    </div>
    <div class="contacts">
      <p><span class="contacts__label">M:</span>0418529647</p>
      <p><span class="contacts__label">E:</span>ross@latherandlore.com.au</p>
      <p><span class="contacts__label">E:</span>edith@latherandlore.com.au</p>
      <p><span class="contacts__label">E:</span>sales@theblokesbalmery.com.au</p>
    </div>
  </section>
</body>
</html>
```